New Website for novelty yarn producer

We need a new website for our company, Merovac. We make highly tailored yarns for weavers worldwide. This year marks our 40th anniversary and we want to evolve our image and identity.

Our temporary website can be found at:
www.merovacyarns-example.com

Our only concern in that throughout the website the protagonist must be our client, we make their creations possible and are highly adaptable both during the ideation process of the yarn as well as in the production. This is at the core of the way we do business and is summarised within the concept of OBM (Open Bridge Method).

Industry/Entity Type

Textile

Number of Pages Required

1 page

Colors
9bcb3c

Requirements
Must have
• Open Bridge Method (OBM) - can be found on or current website www.merovacyarns-example.com

```html
<!DOCTYPE html>
<html lang="en">
<head>
<meta charset="utf-8">
<title>Merovac Yarn Solution</title>
<link href="https://fonts.googleapis.com/css2?family=Cinzel:wght@400;700&family=Open+Sans:wght@400;600;700&display=swap" rel="stylesheet">
<style>
:root{
  --green:#9bcb3c;
  --green-dark:#7fae25;
  --ink:#333;
  --muted:#777;
  --line:#e2e2e2;
  --dark:#2b2a28;
  --darker:#1f1e1c;
  --paper:#fff;
  --soft:#f4f4f4;
}
*{box-sizing:border-box;margin:0;padding:0}
html,body{width:1200px;height:3460px;overflow:hidden}
body{font-family:"Open Sans",sans-serif;color:var(--ink);background:var(--paper);position:relative}
.serif{font-family:"Cinzel",serif}

/* header */
.site-header{position:absolute;top:0;left:0;width:1200px;height:92px;background:var(--paper);z-index:3}
.brand{position:absolute;left:100px;top:14px;display:flex;align-items:center;gap:12px}
.brand-name{font-family:"Cinzel",serif;font-weight:700;font-size:40px;color:var(--dark);letter-spacing:1px}
.brand-tag{position:absolute;left:104px;top:64px;font-size:9px;letter-spacing:2px;color:var(--green);text-transform:uppercase}
.top-contact{position:absolute;right:100px;top:10px;display:flex;gap:26px;font-size:11px;color:var(--muted)}
.top-contact span::before{content:"";display:inline-block;width:8px;height:8px;border-radius:50%;background:var(--green);margin-right:6px}
.main-nav{position:absolute;right:100px;top:50px;display:flex;gap:0}
.main-nav a{display:block;padding:12px 16px;font-size:11px;font-weight:600;letter-spacing:1px;color:var(--ink);text-decoration:none;text-transform:uppercase}
.main-nav a.active{background:var(--green);color:#fff}

/* hero */
.hero{position:absolute;top:92px;left:0;width:1200px;height:570px;background:linear-gradient(135deg,#6f6a5f 0%,#9b968a 35%,#7a7468 60%,#4e4a43 100%)}
.hero-title{position:absolute;top:160px;width:100%;text-align:center;font-family:"Cinzel",serif;font-weight:700;font-size:50px;color:var(--green);letter-spacing:3px}
.hero-sub{position:absolute;top:236px;width:100%;text-align:center;font-family:"Cinzel",serif;font-size:32px;color:#fff;line-height:1.25}
.hero-arrow{position:absolute;top:270px;width:40px;height:60px;background:rgba(0,0,0,.45)}
.hero-arrow.left{left:0}.hero-arrow.right{right:0}
.anniv{position:absolute;left:940px;top:378px;width:130px;height:130px;border-radius:50%;background:var(--green);border:6px solid #fff;color:#fff;text-align:center;font-family:"Cinzel",serif}
.anniv b{display:block;font-size:46px;line-height:1;margin-top:26px}
.anniv small{font-size:11px;letter-spacing:1px}

/* about */
.about{position:absolute;top:580px;left:110px;width:980px;height:720px;background:var(--paper);box-shadow:0 0 12px rgba(0,0,0,.08);text-align:center;z-index:2}
.section-title{font-family:"Cinzel",serif;font-size:42px;color:var(--ink);font-weight:400}
.about .section-title{margin-top:26px}
.about-intro{width:820px;margin:14px auto 0;font-size:12px;line-height:1.7;color:var(--muted)}
.values{display:flex;justify-content:center;gap:60px;margin-top:36px}
.value{width:250px}
.value-icon{width:200px;height:200px;margin:0 auto;border:2px solid var(--line);display:flex;align-items:center;justify-content:center}
.value-art{width:120px;height:120px;border-radius:50%;background:linear-gradient(135deg,#c9e58f,var(--green))}
.value h3{margin-top:22px;font-size:18px;font-weight:700;letter-spacing:1px}
.value p{margin-top:10px;font-size:12px;line-height:1.6;color:var(--muted)}
.btn-outline{display:inline-block;padding:8px 22px;border:1px solid #bbb;font-size:10px;letter-spacing:1px;color:var(--muted);text-transform:uppercase}
.about .btn-outline{margin-top:44px}

/* method */
.method{position:absolute;top:1320px;left:0;width:1200px;height:820px;background:linear-gradient(180deg,#3a3632 0%,#2c2926 50%,#3d3934 100%)}
.method-badge{position:absolute;left:450px;top:0;width:300px;height:130px}
.method-badge-label{position:absolute;left:540px;top:36px;display:flex;align-items:center;gap:14px;z-index:1}
.method-badge-label i{display:block;width:50px;height:50px;border-radius:50%;background:var(--soft)}
.method-badge-label span{font-size:13px;letter-spacing:1px;color:var(--muted);line-height:1.3;text-transform:uppercase}
.method-title{position:absolute;top:188px;width:100%;text-align:center;font-family:"Cinzel",serif;font-size:40px;color:var(--green)}
.method-intro{position:absolute;top:256px;left:180px;width:840px;text-align:center;font-size:12px;line-height:1.7;color:#ddd}
.timeline-axis{position:absolute;left:599px;top:360px;width:2px;height:260px;background:var(--green)}
.timeline-bar{position:absolute;left:0;top:540px;width:1200px;height:20px;background:var(--green)}
.stage{position:absolute;width:300px;color:#ddd;font-size:12px;line-height:1.6}
.stage h4{font-size:15px;color:var(--green);letter-spacing:1px;text-transform:uppercase;margin-bottom:6px}
.stage .btn-outline{margin-top:12px;border-color:#888;color:#ccc}
.stage.ideation{left:110px;top:368px}
.stage.scaling{left:790px;top:368px}
.stage.execution{left:450px;top:600px;width:300px;text-align:center}
.node{position:absolute;width:46px;height:46px;border-radius:50%;background:var(--green);border:4px solid #fff}
.stem{position:absolute;width:2px;background:var(--green)}

/* blog */
.blog{position:absolute;top:2160px;left:0;width:1200px;height:500px;background:var(--paper);text-align:center}
.blog .section-title{margin-top:40px}
.posts{display:flex;justify-content:center;gap:24px;margin-top:30px}
.post{width:306px;text-align:left;box-shadow:0 0 8px rgba(0,0,0,.08);padding-bottom:16px}
.post-photo{height:180px}
.post-photo.p1{background:linear-gradient(135deg,#8a2b27,#c25a3a,#6b1f1c)}
.post-photo.p2{background:linear-gradient(135deg,#c8b9a6,#8b2d3c,#e0d3c2)}
.post-photo.p3{background:linear-gradient(135deg,#d94f6b,#5fae4b,#e6b93a,#3a6bb3)}
.post h5{margin:14px 16px 6px;font-size:12px;font-weight:700;color:var(--ink)}
.post p{margin:0 16px;font-size:11px;line-height:1.6;color:var(--muted)}
.post time{display:block;margin:10px 16px 0;font-size:10px;color:var(--muted)}

/* contact */
.contact{position:absolute;top:2660px;left:0;width:1200px;height:560px;background:var(--soft)}
.contact .section-title{position:absolute;top:60px;width:100%;text-align:center}
.contact-info{position:absolute;left:100px;top:160px;font-size:12px;line-height:1.6;color:var(--muted)}
.contact-info li{list-style:none;display:flex;gap:14px;margin-bottom:26px;align-items:flex-start}
.contact-info svg{flex:none;margin-top:2px}
.contact-form{position:absolute;left:520px;top:160px;width:580px}
.field{height:40px;border:1px solid var(--line);background:#fff;margin-bottom:14px;padding:11px 12px;font-size:11px;color:#aaa}
.field.tall{height:110px}
.btn-submit{height:40px;background:var(--green);color:#fff;text-align:center;font-size:12px;font-weight:700;letter-spacing:1px;line-height:40px}

/* footer */
.site-footer{position:absolute;top:3220px;left:0;width:1200px;height:240px;background:var(--dark);text-align:center}
.footer-nav{display:flex;justify-content:center;gap:50px;padding-top:26px;font-size:11px;color:#bbb}
.footer-brand{margin-top:40px;font-family:"Cinzel",serif;font-weight:700;font-size:58px;color:#fff;letter-spacing:2px}
.social{display:flex;justify-content:center;gap:14px;margin-top:14px}
.social i{width:18px;height:18px;border-radius:50%;background:var(--green)}
.copyright{position:absolute;bottom:14px;width:100%;font-size:10px;color:#888}
</style>
</head>
<body>

<header class="site-header">
  <div class="brand"><span class="brand-name">MEROVAC</span></div>
  <div class="brand-tag">Novelty · Yarn · Solutions</div>
  <div class="top-contact"><span>0555 010 234</span><span>hello@merovac-example.com</span></div>
  <nav class="main-nav">
    <a class="active" href="#about">About</a>
    <a href="#method">Open Bridge Method</a>
    <a href="#story">Our Story</a>
    <a href="#team">Team</a>
    <a href="#work">Work</a>
    <a href="#contact">Contact</a>
  </nav>
</header>

<section class="hero" role="img" aria-label="Close-up photograph of woven yarn samples and fabric swatches">
  <div class="hero-arrow left"></div>
  <div class="hero-arrow right"></div>
  <h1 class="hero-title">MEROVAC YARN SOLUTION</h1>
  <p class="hero-sub">Tailored weaving<br>solutions</p>
  <div class="anniv"><b>40</b><small>ANNIVERSARY</small></div>
</section>

<section class="about" id="about">
  <h2 class="section-title">About Us</h2>
  <p class="about-intro">For forty years we have spun yarns around the ideas of the weavers we work with. Every thread starts from their creation, and our job is to make it possible, adapting each step from the first sample to the final production run so that their fabric turns out exactly as imagined.</p>
  <div class="values">
    <div class="value">
      <div class="value-icon"><div class="value-art" role="img" aria-label="Icon of a group of people with stars"></div></div>
      <h3>EXPERIENCE</h3>
      <p>Over the years the company has gained the knowledge and skill that makes it a partner of our customers and their ideas.</p>
    </div>
    <div class="value">
      <div class="value-icon"><div class="value-art" role="img" aria-label="Icon of a glowing light bulb"></div></div>
      <h3>CREATIVITY</h3>
      <p>Over the years the company has gained the knowledge and skill that makes it a partner of our customers and their ideas.</p>
    </div>
    <div class="value">
      <div class="value-icon"><div class="value-art" role="img" aria-label="Icon of a necktie"></div></div>
      <h3>PROFESSIONALITY</h3>
      <p>Over the years the company has gained the knowledge and skill that makes it a partner of our customers and their ideas.</p>
    </div>
  </div>
  <span class="btn-outline">Read more</span>
</section>

<section class="method" id="method" role="img" aria-label="Dark photograph of yarn spinning machinery">
  <svg class="method-badge" viewBox="0 0 300 130"><polygon points="0,0 300,0 300,90 150,130 0,90" fill="#fff"/></svg>
  <div class="method-badge-label"><i></i><span>Open<br>Bridge<br>Method</span></div>
  <h2 class="method-title">MNYS Open Bridge Method</h2>
  <p class="method-intro">We believe that the key to spinning a yarn is to start from our client's idea and work beside them through every step, from the first sketch to the finished cone. The OBM keeps us flexible and open, so the creation always stays in their hands.</p>

  <div class="timeline-axis"></div>
  <div class="timeline-bar"></div>

  <div class="stage ideation">
    <h4>Ideation</h4>
    <p>Alongside our client's expectations we work together with weavers from day one, sharing sketches and samples until the yarn is right.</p>
    <span class="btn-outline">Read more</span>
  </div>
  <div class="node" style="left:577px;top:410px"></div>

  <div class="stage scaling">
    <h4>Scaling production</h4>
    <p>Alongside our client's expectations we scale each yarn to full production, keeping quality and timing as agreed.</p>
    <span class="btn-outline">Read more</span>
  </div>

  <div class="stem" style="left:180px;top:560px;height:70px"></div>
  <div class="node" style="left:157px;top:620px"></div>
  <div class="stem" style="left:1010px;top:560px;height:70px"></div>
  <div class="node" style="left:987px;top:620px"></div>

  <div class="stage execution">
    <h4>Execution</h4>
    <p>Alongside our client's expectations we deliver each order with care and follow it until the fabric is woven.</p>
    <span class="btn-outline">Read more</span>
  </div>
</section>

<section class="blog">
  <h2 class="section-title">Our Blog</h2>
  <div class="posts">
    <article class="post">
      <div class="post-photo p1" role="img" aria-label="Photograph of red twisted yarn"></div>
      <h5>MEROVAC 1976 – 40 YEARS IN THE MAKING</h5>
      <p>Merovac was founded in 1976 and has since supplied fine novelty yarns to weavers across the world.</p>
      <time>Posted on March 12, 2016</time>
    </article>
    <article class="post">
      <div class="post-photo p2" role="img" aria-label="Photograph of woven fabric swatches"></div>
      <h5>MEROVAC 1976 – 40 YEARS IN THE MAKING</h5>
      <p>Merovac was founded in 1976 and has since supplied fine novelty yarns to weavers across the world.</p>
      <time>Posted on March 12, 2016</time>
    </article>
    <article class="post">
      <div class="post-photo p3" role="img" aria-label="Photograph of colourful yarn cones"></div>
      <h5>MEROVAC 1976 – 40 YEARS IN THE MAKING</h5>
      <p>Merovac was founded in 1976 and has since supplied fine novelty yarns to weavers across the world.</p>
      <time>Posted on March 12, 2016</time>
    </article>
  </div>
</section>

<section class="contact" id="contact">
  <h2 class="section-title">Contact Us</h2>
  <ul class="contact-info">
    <li><svg width="16" height="20" viewBox="0 0 16 20"><path d="M8 0a7 7 0 0 0-7 7c0 5 7 13 7 13s7-8 7-13a7 7 0 0 0-7-7z" fill="#9bcb3c"/><circle cx="8" cy="7" r="2.5" fill="#fff"/></svg>
      <span>Merovac Novelty Yarn Solutions<br>Via Filatura 12<br>Prato Nord<br>Italy</span></li>
    <li><svg width="18" height="14" viewBox="0 0 18 14"><rect width="18" height="14" fill="#9bcb3c"/><path d="M0 0l9 7 9-7" stroke="#fff" fill="none"/></svg>
      <span>hello@merovac-example.com</span></li>
    <li><svg width="16" height="16" viewBox="0 0 16 16"><path d="M3 0l3 4-2 2c1 2 4 5 6 6l2-2 4 3-2 3C7 16 0 9 0 3z" fill="#9bcb3c"/></svg>
      <span>0555 010 234</span></li>
  </ul>
  <form class="contact-form">
    <div class="field">Type your Name</div>
    <div class="field">Type your Email</div>
    <div class="field">Type your Subject</div>
    <div class="field tall">Type your Message</div>
    <div class="btn-submit">SUBMIT</div>
  </form>
</section>

<footer class="site-footer">
  <nav class="footer-nav"><span>About</span><span>Open Bridge Method</span><span>Our Story</span><span>Team</span><span>Blog</span><span>Contact</span></nav>
  <div class="footer-brand">MEROVAC</div>
  <div class="social"><i></i><i></i><i></i></div>
  <p class="copyright">© Copyright 2016 · All rights reserved</p>
</footer>

</body>
</html>
```